Restaurant needs a vertical banner for fried catfish

Our restaurant is looking for an eye-catching 78.75in. x 36in. vertical physical banner ad for our fried catfish. Photos for the fried catfish will be provided as a reference but we will also accept anything similar to the photo. We will be using the following as our receptacle: https://www.plorvista.com/banner-stand/retractable-banner-stands/
The design must incorporate the following flavor texts:
Fried Catfish
Always Fresh!
Made from Scratch
Hand-cut Fillets
The Best Catfish in Texas
Served with fries, hush puppies, and a 32oz fountain drink
Also available by the pound!
The final design should be creative, professional, and eye-catching for customers.
Updates
Need extra days to review
Colors
Designer to choose colors to be used in the design.
Requirements
Must have
- We are open to any and all design elements, albeit the 'flavor texts' should not overpower, but complement the fried catfish photo. 'Fried Catfish' can be used in lieu of a main title/logo.
Nice to have
- Transparent or textured backgrounds that can encompass any or all part of the banner such as a cutting board, shadows, abstract, etc to show depth are a plus.
- Use of vectors or objects such as ribbons or shapes to encapsulate the 'flavor texts' are also encouraged.

```html
<!DOCTYPE html>
<html lang="en">
<head>
<meta charset="utf-8">
<title>Fried Catfish – Vertical Banner</title>
<link rel="stylesheet" href="https://fonts.googleapis.com/css2?family=Montserrat:wght@600;800&family=Source+Sans+3:wght@400&display=swap">
<style>
  :root {
    --canvas-bg: #cac9cc;
    --brand-red: #a3272a;
    --deep-red: #85201f;
    --strip-red: #b02a2c;
    --ink: #111111;
    --text-light: #ffffff;
    --mist-top: #f1f0ef;
    --mist-low: #e4e1df;
    --food-gold: #d9a04a;
    --food-amber: #c57f36;
    --plate-red: #9b3a3a;
  }
  * { margin: 0; padding: 0; box-sizing: border-box; }
  html, body {
    width: 1200px;
    height: 1200px;
    overflow: hidden;
    background: var(--canvas-bg);
  }
  .banner-frame {
    position: absolute;
    left: 342px;
    top: 36px;
    width: 560px;
    height: 1225px;
    transform: scale(0.92);
    transform-origin: 0 0;
    overflow: hidden;
  }
  .banner-art {
    position: absolute;
    inset: 0;
    width: 560px;
    height: 1225px;
    display: block;
  }
  .headline {
    position: absolute;
    left: 0;
    top: 118px;
    width: 560px;
    text-align: center;
  }
  .headline-main {
    display: block;
    font-family: "Montserrat", sans-serif;
    font-weight: 800;
    font-size: 184px;
    line-height: 1;
    letter-spacing: 1px;
    color: var(--brand-red);
    margin-left: 6px;
  }
  .headline-rule {
    width: 486px;
    height: 4px;
    background: var(--ink);
    margin: 16px auto 0 50px;
  }
  .headline-sub {
    display: block;
    font-family: "Source Sans 3", sans-serif;
    font-weight: 400;
    font-size: 44px;
    line-height: 1;
    letter-spacing: 0.42em;
    color: var(--ink);
    margin-top: 16px;
    padding-left: 18px;
  }
  .flavor-list {
    position: absolute;
    left: 52px;
    top: 920px;
    list-style: none;
    font-family: "Montserrat", sans-serif;
    font-weight: 600;
    font-size: 24px;
    line-height: 28.8px;
    letter-spacing: 0.06em;
    color: var(--text-light);
  }
</style>
</head>
<body>
  <div class="banner-frame">
    <svg class="banner-art" viewBox="0 0 560 1225" xmlns="http://www.w3.org/2000/svg">
      <defs>
        <linearGradient id="photoTone" x1="0" y1="0" x2="0" y2="1">
          <stop offset="0" stop-color="var(--mist-top)"/>
          <stop offset="0.42" stop-color="var(--mist-low)"/>
          <stop offset="0.58" stop-color="var(--food-gold)"/>
          <stop offset="0.8" stop-color="var(--food-amber)"/>
          <stop offset="1" stop-color="var(--plate-red)"/>
        </linearGradient>
      </defs>
      <rect x="0" y="0" width="560" height="960" fill="url(#photoTone)" role="img" aria-label="Photo of golden fried catfish pieces with red chili peppers on a plate, soft blurred restaurant background"/>
      <path class="corner-accent" d="M290 0 L560 0 L560 92 C470 62 380 30 290 0 Z" fill="var(--brand-red)"/>
      <path class="wave-ribbon" d="M0 364 C140 352 320 500 560 526 L560 544 C330 520 150 396 0 392 Z" fill="var(--brand-red)"/>
      <path class="info-panel" d="M0 795 C130 815 310 905 560 880 L560 1225 L0 1225 Z" fill="var(--deep-red)"/>
      <path class="info-panel-edge" d="M0 795 C130 815 310 905 560 880" fill="none" stroke="var(--strip-red)" stroke-width="3"/>
      <rect class="base-strip" x="0" y="1214" width="560" height="11" fill="var(--strip-red)"/>
    </svg>

    <header class="headline">
      <h1 class="headline-main">Fried</h1>
      <div class="headline-rule"></div>
      <span class="headline-sub">CATFISH</span>
    </header>

    <ul class="flavor-list">
      <li>Fried Catfish</li>
      <li>Always Fresh!</li>
      <li>Made from Scratch</li>
      <li>Hand-cut Fillets</li>
      <li>The Best Catfish in</li>
      <li>Texas Served with</li>
      <li>fries, hush puppies,</li>
      <li>and a 32oz fountain drink</li>
      <li>Also available by the pound!</li>
    </ul>
  </div>
</body>
</html>
```